Brisvane Partners Web Design

Dear all
I need a web design for a financial services site. We are a broker who deals with many different financial institutions and require a clean, simple and instantly impressive site based on the colour scheme that Mockwell created for us. A landing page (www.brisvn.mx) gives an idea of the logo and clour scheme but we are looking at either a one page site with rollover text boxes or a 3 or 4 page site depending on the preference of the designer and the best user experience. The site“s purpose is to give confidence that the company exists rather than impart pages of information although we would like this to be a site that can expand over time as the company grows. For now the requirement is for a clear set of possibly changing images at the centre of a white screen that relate to finance in general nad the benefits of wealth creation as well as sectios either along the top or bottom - Our Company, Our Approach, Our services, Our clients, Contact (user to fill in contact box to be sent to info@brisvn.mx. The text for each of these boxes I assume can be added by the coding team here, it the overall look and feel that I am looking for from Mockwell - deadline can be extended if necessary but I was hoping to wrap this all up in October

Target Market(s)

Succesful individuals looking to maximise returns on their investment via world class financial institutions and supported throughout by qualified independent financial advisors

Industry/Entity Type

Finance

Requirements
Must have
• Logo and color scheme of the logo design Mockwell sent - I have all these sourcefiles, pantone and fonts

```html
<!DOCTYPE html>
<html lang="en">
<head>
<meta charset="utf-8">
<title>Brisvane Partners</title>
<link href="https://fonts.googleapis.com/css2?family=PT+Sans:wght@400;700&display=swap" rel="stylesheet">
<style>
:root{
  --navy:#1f4479;
  --ink:#2c3b58;
  --text:#6f6f6f;
  --muted:#a9a9a9;
  --line:#dcdcdc;
  --btn:#4d5157;
  --footer:#5c5f64;
  --field:#f7f7f7;
  --accent:#d2541c;
}
*{box-sizing:border-box;margin:0;padding:0}
html,body{width:1006px;height:1200px;overflow:hidden;background:#fff}
body{font-family:"PT Sans",sans-serif;color:var(--text);position:relative}
.abs{position:absolute}
.brand{left:152px;top:18px;width:130px;color:var(--navy);font-size:15px;letter-spacing:5px;line-height:18px}
.brand .mark{width:22px;height:22px;background:var(--navy);margin:0 0 8px 50px}
.brand small{display:block;font-size:7px;letter-spacing:3px;line-height:10px;padding-left:40px}
.social{left:464px;top:22px;display:flex;gap:4.8px}
.social span{width:16px;height:16px;border-radius:50%;background:#d6d6d6}
.quick{left:626px;top:21px;font-size:14px;color:var(--muted);display:flex;align-items:center;gap:6px}
.quick b{color:var(--navy);font-weight:400}
.nav{top:64px;left:0;font-size:10px;color:var(--ink)}
.nav a{position:absolute;top:0;height:22px;line-height:22px;white-space:nowrap;color:inherit;text-decoration:none}
.nav a.on{background:#435a7f;color:#fff;width:62px;text-align:center;border-radius:2px}
.rule{left:0;width:1006px;height:1px;background:var(--line)}
.hero{left:0;top:100px;width:1006px;height:376px;background:linear-gradient(100deg,#c9cfd8 0%,#e2dcd4 25%,#b7a48e 45%,#6c8fb6 65%,#dcc3b0 85%,#8fa4bd 100%)}
.arrow{width:36px;height:36px;border:2px solid rgba(255,255,255,.5);border-radius:50%;top:274px}
.cap{left:154px;background:rgba(40,58,92,.85);color:#fff;font-size:13.5px;padding:0 22px;line-height:32px}
.feat{top:506px;width:230px}
.feat .ico{width:43px;height:42px;background:var(--navy);position:absolute;left:0;top:0;display:flex;align-items:center;justify-content:center}
.feat h3{position:absolute;left:59px;top:0;font-weight:400;font-size:14px;color:var(--navy);white-space:nowrap}
.feat p{position:absolute;left:60px;top:24px;width:160px;font-size:7.4px;line-height:12.8px}
h2{position:absolute;font-weight:400;font-size:14px;color:var(--navy)}
.copy{font-size:7.4px;line-height:12.8px}
.btn{background:var(--btn);color:#fff;font-size:7.5px;text-align:center;line-height:23px;height:23px;width:78px;border-radius:2px}
.photo{left:470px;top:664px;width:151px;height:72px;background:linear-gradient(180deg,#7d9bc4 0%,#b7c5d8 50%,#4b5562 100%)}
.card{width:222px;height:172px;border:1px solid var(--line);background:#f7f7f7;padding:22px 21px}
.card h4{font-weight:400;font-size:8px;color:var(--navy)}
.card em{display:block;font-size:8px;color:var(--accent);margin:7px 0 11px}
.field{left:634px;width:222px;height:21px;border:1px solid var(--line);background:var(--field);font-size:8px;color:#666;padding:4px 11px}
.partner{top:1094px;font-size:19px;color:#8c8c8c;display:flex;align-items:center;gap:6px;white-space:nowrap}
.partner i{width:20px;height:20px;background:#a6a6a6;display:block}
.footer{left:0;top:1148px;width:1006px;height:52px;background:var(--footer);color:#fff;font-size:7px}
.footer nav{position:absolute;left:152px;top:22px;display:flex;gap:13px}
.footer .copy-r{position:absolute;left:738px;top:22px}
</style>
</head>
<body>
<div class="abs brand"><div class="mark"></div>BRISVANE<small>PARTNERS</small></div>
<div class="abs social"><span></span><span></span><span></span><span></span><span></span><span></span><span></span></div>
<div class="abs quick"><svg width="16" height="16" viewBox="0 0 16 16"><path d="M3 1l3 3-2 2c1 2 3 4 5 5l2-2 3 3-2 3C7 15 1 9 1 3z" fill="#c8c8c8"/></svg>Quick contact : <b>+52 (55) 4100 2275</b></div>
<div class="abs nav">
  <a class="on" style="left:314px">Home</a>
  <a style="left:405px">Our Company</a>
  <a style="left:510px">Our Approach</a>
  <a style="left:617px">Our services</a>
  <a style="left:714px">Our clients</a>
  <a style="left:806px">Contact</a>
</div>
<div class="abs rule" style="top:100px"></div>

<div class="abs hero" role="img" aria-label="Photo of three smiling friends talking together"></div>
<div class="abs arrow" style="left:70px"></div>
<div class="abs arrow" style="left:890px"></div>
<div class="abs cap" style="top:374px">WE ARE BROKERS</div>
<div class="abs cap" style="top:414px">AND DEAL WITH LOTS OF FINANCIAL INSTITUTIONS.</div>

<div class="abs feat" style="left:152px">
  <div class="ico"><svg width="22" height="24" viewBox="0 0 22 24" fill="none" stroke="#fff" stroke-width="1.4"><circle cx="11" cy="10" r="6"/><path d="M8 17h6M9 20h4M11 1v2M2 10h2M18 10h2M4 3l1.5 1.5M18 3l-1.5 1.5"/></svg></div>
  <h3>Specialty Finance</h3>
  <p>Now use Lorem Ipsum as their default model text, and a search for 'lorem ipsum' will uncover many web sites still in their infancy. Various versions have evolved...</p>
</div>
<div class="abs feat" style="left:395px">
  <div class="ico"><svg width="22" height="24" viewBox="0 0 22 24"><circle cx="11" cy="7" r="5" fill="#fff"/><path d="M2 23c0-6 4-9 9-9s9 3 9 9z" fill="#fff"/></svg></div>
  <h3>Broker dealer</h3>
  <p>Now use Lorem Ipsum as their default model text, and a search for 'lorem ipsum' will uncover many web sites still in their infancy. Various versions have evolved...</p>
</div>
<div class="abs feat" style="left:638px">
  <div class="ico"><svg width="26" height="24" viewBox="0 0 26 24" fill="#fff"><rect x="2" y="16" width="3" height="7"/><rect x="7" y="13" width="3" height="10"/><rect x="12" y="14" width="3" height="9"/><rect x="17" y="10" width="3" height="13"/><rect x="22" y="6" width="3" height="17"/><path d="M2 12l6-5 5 3 10-8" stroke="#fff" stroke-width="1.5" fill="none"/></svg></div>
  <h3>Corporate &amp; Investment</h3>
  <p>Now use Lorem Ipsum as their default model text, and a search for 'lorem ipsum' will uncover many web sites still in their infancy. Various versions have evolved...</p>
</div>
<div class="abs rule" style="top:600px"></div>

<h2 style="left:152px;top:632px">Our Company</h2>
<div class="abs copy" style="left:153px;top:661px;width:278px">It is a long established fact that a reader will be distracted by the readable content of a page when looking at its layout. The point of using Lorem Ipsum is that it has a more-or-less normal distribution of letters, as opposed to using 'Content here, content here', making it look like readable English. Many desktop publishing packages and web page editors now use Lorem Ipsum as their default model text...<br><br>Various versions have evolved over the years, sometimes by accident, sometimes on purpose uncover many web sites still in their infancy. Various versions have evolved over the years, sometimes by accident, sometimes on purpose...</div>
<div class="abs btn" style="left:152px;top:789px">READ MORE</div>

<h2 style="left:468px;top:632px">Our Approach</h2>
<div class="abs photo" role="img" aria-label="Photo of office towers seen from street level"></div>
<div class="abs copy" style="left:642px;top:663px;width:213px">It is a long established fact that a reader will be distracted by the readable content of a page when looking at its layout. The point of using Lorem Ipsum is that it has a more-or-less normal distribution of letters, as opposed to using 'Content here, content here', making it look like readable English. Many desktop publishing packages and web page editors now use Lorem</div>
<div class="abs copy" style="left:469px;top:749px;width:380px">It is a long established fact that a reader will be distracted by the readable content of a page when looking at its layout. The point of using Lorem Ipsum is that it has a more-or-less normal distribution....</div>
<div class="abs btn" style="left:468px;top:790px">READ MORE</div>

<h2 style="left:150px;top:849px">Happy Clients</h2>
<svg class="abs" style="left:594px;top:856px" width="20" height="10" viewBox="0 0 20 10" fill="none" stroke="#aaa" stroke-width="1.2"><path d="M6 2L3 5l3 3M14 2l3 3-3 3"/></svg>
<div class="abs card" style="left:152px;top:886px">
  <h4>CONSECTETUR ADIPISCING ELIT</h4><em>20 AUG 2013</em>
  <p class="copy" style="color:#555">Lorem ipsum dolor sit amet, consectetur adipiscing elit. Pellentesque tempus eu mauris at tempus. Nulla facilisi. Ut auctor dui vel diam cursus tempor. Nulla sit amet diam sit amet turpis.<br><br>Lorem ipsum dolor sit amet, consectetur adipiscing elit. Pellentesque tempus eu mauris...</p>
</div>
<div class="abs card" style="left:393px;top:886px">
  <h4>CONSECTETUR ADIPISCING ELIT</h4><em>20 AUG 2013</em>
  <p class="copy" style="color:#555">Lorem ipsum dolor sit amet, consectetur adipiscing elit. Pellentesque tempus eu mauris at tempus. Nulla facilisi. Ut auctor dui vel diam cursus tempor. Nulla sit amet diam sit amet turpis.<br><br>Lorem ipsum dolor sit amet, consectetur adipiscing elit. Pellentesque tempus eu mauris...</p>
</div>

<h2 style="left:634px;top:849px">Quick Contact</h2>
<div class="abs field" style="top:886px">Name :</div>
<div class="abs field" style="top:919px">Email :</div>
<div class="abs field" style="top:951px">Phone :</div>
<div class="abs field" style="top:982px;height:49px">Message</div>
<div class="abs btn" style="left:778px;top:1041px;width:79px">SUBMIT NOW</div>

<div class="abs partner" style="left:156px"><i></i>Lumora</div>
<div class="abs partner" style="left:303px"><i></i>Veltrix</div>
<div class="abs partner" style="left:450px"><i></i>Orbisan</div>
<div class="abs partner" style="left:598px"><i></i>Kestrel</div>
<div class="abs partner" style="left:731px"><i></i>Halden Hub</div>

<footer class="abs footer">
  <nav><span>HOME</span><span>|</span><span>OUR COMPANY</span><span>|</span><span>OUR APPROACH</span><span>|</span><span>OUR SERVICES</span><span>|</span><span>OUR CLIENTS</span><span>|</span><span>CONTACT</span></nav>
  <div class="copy-r">© BRISVN 2013. ALL RIGHTS RESERVED.</div>
</footer>
</body>
</html>
```